new letterhead/envelope/business card design for law firm

please see attached pdf of current letterhead, envelope and business card. I am also attaching my new logo that I would like to be used. basically, I am looking to refresh and simplify my letterhead/stationary and business card, keeping the following in mind:

overall, I am going for the following look:

-simple,
-modern,
-classy,
-professional

Target Market(s)

law firm clients

Industry/Entity Type

Law Firm

Contact Information for Business Card

see attachment

Font styles to use
Sans Serif

Requirements
Must have
• overall, I am going for the following look:
• -simple,
• -modern,
• -classy,
• -professional
Nice to have
• same as above
Should not have
• no serif fonts

```html
<!DOCTYPE html>
<html lang="en">
<head>
<meta charset="utf-8">
<title>Hollis Law Envelope</title>
<link href="https://fonts.googleapis.com/css2?family=Mulish:wght@400;800&display=swap" rel="stylesheet">
<style>
  :root {
    --navy: #03284f;
    --paper: #ffffff;
    --backdrop: #e9e4dc;
    --shadow: rgba(40, 30, 20, 0.18);
  }
  html, body {
    margin: 0;
    padding: 0;
    width: 1200px;
    height: 900px;
    overflow: hidden;
    background: var(--backdrop);
  }
  .canvas {
    position: relative;
    width: 1200px;
    height: 900px;
  }
  .envelope {
    position: absolute;
    left: 167px;
    top: 194px;
    width: 866px;
    height: 510px;
  }
  .envelope-flap {
    position: absolute;
    left: 0;
    top: 0;
    width: 866px;
    height: 124px;
  }
  .envelope-body {
    position: absolute;
    left: 0;
    top: 122px;
    width: 866px;
    height: 388px;
    background: var(--paper);
    box-shadow: 0 4px 10px var(--shadow);
  }
  .return-address {
    position: absolute;
    left: 40px;
    top: 30px;
    width: 236px;
    text-align: center;
    font-family: "Mulish", sans-serif;
    color: var(--navy);
  }
  .brand-mark {
    display: block;
    width: 62px;
    height: 62px;
    margin: 0 auto 10px;
    border-radius: 50%;
    background: var(--navy);
  }
  .brand-name {
    margin: 0 0 18px;
    font-weight: 800;
    font-size: 29px;
    letter-spacing: 3px;
    line-height: 1;
  }
  .address-line {
    margin: 0;
    font-weight: 400;
    font-size: 17px;
    line-height: 23px;
    white-space: nowrap;
  }
</style>
</head>
<body>
  <div class="canvas">
    <div class="envelope">
      <svg class="envelope-flap" viewBox="0 0 866 124" aria-hidden="true">
        <path d="M0 124 L0 90 Q4 58 40 48 L395 3 Q433 -2 471 3 L826 48 Q862 58 866 90 L866 124 Z" fill="var(--navy)"/>
      </svg>
      <div class="envelope-body">
        <div class="return-address">
          <span class="brand-mark"></span>
          <p class="brand-name">HOLLIS LAW</p>
          <p class="address-line">820 Larkspur Avenue</p>
          <p class="address-line">Suite 410, Raleigh, NC 27605</p>
        </div>
      </div>
    </div>
  </div>
</body>
</html>
```